Poster Design Project

Simple, very easy design project.

Design for a 20" x 30" poster (I will print the poster, you do the high-res design), of the attached.

(Pls note, this JPG is sideways and is an error). You are designing PORTRAIT

```html
<!DOCTYPE html>
<html lang="en">
<head>
<meta charset="utf-8">
<title>Great Ecommerce Poster</title>
<link href="https://fonts.googleapis.com/css2?family=Nunito:wght@900&family=Arimo:wght@400;700&display=swap" rel="stylesheet">
<style>
  :root {
    --band-top: #0696d2;
    --band-bottom: #27c3f0;
    --title-fill: #ffffff;
    --title-edge: #86def8;
    --accent: #1cb7e5;
    --paper: #ffffff;
    --art-core: #7fcbeb;
    --art-mid: #b5e2f5;
    --art-warm: #f6d9a8;
    --art-green: #bfe3a6;
    --art-edge: #e9f6fc;
    --footer: #16b5e5;
  }
  html, body {
    margin: 0;
    padding: 0;
    overflow: hidden;
    background: var(--paper);
  }
  .poster {
    position: relative;
    width: 800px;
    height: 1200px;
    overflow: hidden;
    background: var(--paper);
    font-family: "Arimo", Arial, sans-serif;
  }
  .header {
    position: absolute;
    left: 0;
    top: 0;
    width: 800px;
    height: 280px;
  }
  .values {
    position: absolute;
    top: 302px;
    left: 0;
    width: 800px;
    margin: 0;
    padding: 0;
    list-style: none;
    text-align: center;
    color: var(--accent);
    font-weight: 700;
    font-size: 46px;
    letter-spacing: 3px;
    line-height: 47px;
  }
  .feature-art {
    position: absolute;
    left: 110px;
    top: 605px;
    width: 590px;
    height: 495px;
    border-radius: 46% / 48%;
    background:
      radial-gradient(circle at 72% 30%, var(--art-green) 0%, rgba(191,227,166,0) 28%),
      radial-gradient(circle at 62% 82%, var(--art-warm) 0%, rgba(246,217,168,0) 26%),
      radial-gradient(ellipse at center, var(--art-core) 0%, var(--art-mid) 45%, var(--art-edge) 72%, var(--paper) 100%);
  }
  .footer {
    position: absolute;
    left: 0;
    bottom: 0;
    width: 800px;
    height: 90px;
  }
  .footer-label {
    position: absolute;
    left: 0;
    bottom: 24px;
    width: 800px;
    text-align: center;
    color: #ffffff;
    font-size: 24px;
    letter-spacing: 0.5px;
  }
</style>
</head>
<body>
<main class="poster">
  <svg class="header" viewBox="0 0 800 280" aria-labelledby="poster-title">
    <defs>
      <linearGradient id="band-gradient" x1="0" y1="0" x2="0" y2="1">
        <stop offset="0" stop-color="var(--band-top)"/>
        <stop offset="1" stop-color="var(--band-bottom)"/>
      </linearGradient>
    </defs>
    <path d="M0 0 H800 V240 Q400 228 0 250 Z" fill="url(#band-gradient)"/>
    <path d="M0 256 Q400 236 800 248" fill="none" stroke="var(--band-bottom)" stroke-width="3"/>
    <text id="poster-title" font-family="Nunito, sans-serif" font-weight="900" text-anchor="middle"
          fill="var(--title-fill)" stroke="var(--title-edge)" stroke-width="10"
          paint-order="stroke" stroke-linejoin="round">
      <tspan x="402" y="138" font-size="118" textLength="405" lengthAdjust="spacingAndGlyphs">GREAT</tspan>
      <tspan x="403" y="222" font-size="104" textLength="630" lengthAdjust="spacingAndGlyphs">ECOMMERCE</tspan>
    </text>
  </svg>

  <ul class="values">
    <li>Diversity Of Thought</li>
    <li>Desire To Learn</li>
    <li>Never Settle</li>
    <li>Be A Problem Solver</li>
    <li>Work Fast (web Speed)</li>
    <li>Execution - A Way Of Life</li>
  </ul>

  <div class="feature-art" role="img" aria-label="Illustration of a laptop showing a growth chart, surrounded by colourful app icons"></div>

  <svg class="footer" viewBox="0 0 800 90" aria-hidden="true">
    <path d="M0 12 Q400 -8 800 12 V90 H0 Z" fill="var(--footer)"/>
  </svg>
  <div class="footer-label">CONTACTS</div>
</main>
</body>
</html>
```